GLA

Please send us some options for letterhead I attached our Logo. In addition to the Logo we need this information somewhere on the page

48 Harlow Lane
Fairhaven, MA 06417
555-274-9160

```html
<!DOCTYPE html>
<html lang="en">
<head>
<meta charset="utf-8">
<title>GLA Letterhead</title>
<link rel="stylesheet" href="https://fonts.googleapis.com/css2?family=Tinos&family=Lato:wght@400;700&display=swap">
<style>
  :root {
    --backdrop: #e8e9eb;
    --paper: #ffffff;
    --paper-tint: #eef7fc;
    --ink: #3a3a3a;
    --brand-dark: #4f4340;
    --brand-grey: #6d6d6d;
    --band: #4fc9ef;
    --muted: #777777;
  }
  * { margin: 0; padding: 0; box-sizing: border-box; }
  html, body {
    width: 1200px; height: 960px; overflow: hidden;
    background: var(--backdrop);
  }
  .letterhead {
    position: absolute; left: 280px; top: 28px;
    width: 640px; height: 904px;
    background: var(--paper);
    box-shadow: 0 2px 8px rgba(0,0,0,0.18);
    overflow: hidden;
  }
  .letterhead__tint {
    position: absolute; left: 0; right: 0; top: 130px; bottom: 20px;
    background: linear-gradient(180deg, var(--paper) 0%, var(--paper-tint) 30%, var(--paper-tint) 100%);
  }
  .brand {
    position: absolute; left: 276px; top: 52px;
    display: flex; align-items: center; gap: 12px;
  }
  .brand__mark {
    width: 66px; height: 66px; background: var(--brand-dark);
  }
  .brand__name {
    font-family: "Lato", sans-serif; font-weight: 700;
    font-size: 36px; letter-spacing: 2px; color: var(--brand-grey);
  }
  .letter-body {
    position: absolute; left: 68px; right: 74px; top: 196px;
    font-family: "Tinos", serif; font-size: 9.6px; line-height: 12.9px;
    color: var(--ink); text-align: justify; hyphens: auto;
  }
  .letter-body p + p { margin-top: 12.9px; }
  .signature {
    position: absolute; left: 425px; top: 632px;
    width: 92px; height: 54px;
    background: linear-gradient(90deg, rgba(60,60,60,0.10), rgba(60,60,60,0.04));
    border-radius: 4px;
  }
  .sender-address {
    position: absolute; left: 0; right: 0; top: 838px;
    font-family: "Lato", sans-serif; font-size: 10px; line-height: 13px;
    font-style: normal;
    color: var(--muted); text-align: center;
  }
  .letterhead__band {
    position: absolute; left: 0; right: 0; bottom: 0; height: 20px;
    background: var(--band);
  }
</style>
</head>
<body>
  <main class="letterhead">
    <div class="letterhead__tint" role="img" aria-label="Faint pale blue sunburst decoration behind the letter"></div>

    <header class="brand">
      <div class="brand__mark"></div>
      <span class="brand__name">GLA</span>
    </header>

    <section class="letter-body">
      <p>Lorem ipsum dolor sit amet, consectetur adipiscing elit. Vivamus eget lacus ut velit semper congue a sed lectus. Fusce ut eleifend est, quis volutpat risus. Cras posuere pellentesque vulputate. Suspendisse accumsan tortor et elementum semper. Maecenas vitae arcu sed nulla facilisis fringilla sit amet vel quam. Pellentesque ornare, nibh et dapibus facilisis, augue ipsum varius orci, vitae molestie mi leo ut est. Vivamus facilisis augue erat. Mauris vitae consequat sem. Curabitur sollicitudin augue erat, a viverra elit feugiat a. Nunc lacinia tincidunt felis, eu molestie dui vehicula eu. Donec elementum quis ante eu feugiat. Integer egestas eu lectus quis imperdiet. Sed sed nisl nulla. Mauris eu dapibus erat, at consectetur leo. Vestibulum luctus interdum velit, vitae dictum nisi ultricies nec.</p>
      <p>Nulla commodo ultricies nulla, eget luctus nunc vestibulum eu. Etiam interdum augue nibh, nec fringilla est tempor at. Nullam in risus quam. Fusce lobortis dignissim ultricies. Maecenas at augue sit amet odio pellentesque tempus tempor at nunc. Nullam ligula justo, faucibus vitae risus quis, iaculis semper nisi. Donec eu porta nulla, eu molestie massa. Nam hendrerit non metus a porta. Sed vitae gravida felis, vel posuere purus. Vivamus ac eros ac lectus feugiat placerat et non erat. Pellentesque vitae consectetur nulla. Nulla et suscipit sem.</p>
      <p>Quisque sit amet sagittis enim. Curabitur nisl tellus, vestibulum in lorem consequat, fringilla tempus quam. Aliquam erat volutpat. Nullam ut quam vel lacus pulvinar tincidunt nec ac neque. Donec hendrerit massa nulla, ut venenatis enim ultricies ac. Etiam malesuada iaculis elit, sed molestie augue pulvinar sed. Aenean sed congue mauris, aliquam feugiat nulla. Fusce lobortis libero nunc, sit amet molestie nulla tristique eu.</p>
      <p>Cras eu sapien a lorem blandit dapibus nec nec neque. Proin at consectetur nisl, ut porttitor felis. Proin eleifend semper massa nec ultricies. Nullam id imperdiet lectus, ut consectetur dui. Sed consectetur, sapien sed tristique consequat, nibh dolor ullamcorper justo, ac viverra velit velit vel lorem. Sed nec luctus ipsum. Mauris et tempor ante. Cras porta ullamcorper nisl, vel pellentesque mauris iaculis quis. Curabitur gravida malesuada orci, sit amet commodo massa hendrerit sed. Sed posuere diam metus. Maecenas tristique enim non lacus mollis, tristique bibendum quam varius. Praesent ut adipiscing neque, ut porta dui. Integer in tellus vestibulum, blandit urna ut, dapibus magna. Fusce ut semper nibh. Ut venenatis elit quis lectus condimentum consequat. Etiam mollis convallis massa vel tristique.</p>
      <p>Proin a nibh felis. In lacinia rutrum lectus, vitae luctus purus imperdiet eget. Maecenas ut mi felis. Aliquam erat volutpat. Sed tempor urna sit amet orci rhoncus convallis. Vivamus tempus sapien sed mi suscipit, eget adipiscing odio suscipit. Nunc justo lorem, adipiscing a cursus sed, elementum quis erat. Sed at lectus sit amet nisl vehicula adipiscing. Nulla sodales neque a est suscipit rhoncus.</p>
    </section>

    <div class="signature" role="img" aria-label="Handwritten signature"></div>

    <address class="sender-address">
      48 Harlow Lane<br>
      Fairhaven, MA 06417<br>
      555-274-9160
    </address>

    <div class="letterhead__band"></div>
  </main>
</body>
</html>
```